Stationery Design Project

I am looking for stationary design for an automotive collision repair company. This needs to work with my business cards just designed here. I've attached. I need 8.5 x 11 stationary and corissponding envelopes. a jot tab note pad also. Our companies focus is very high end customer service driven . Our customer base is 35-65 middle to high income. Please include company name, logo, address, phone number, web address. The business card is two greys with green and white writing. I invision a light grey background with a darker grey band on it that contains the logo.
Updates

I justĀ 

Why is no one touching this project

Target Market(s)

60%. Women 40% men. Age 35-60

Industry/Entity Type

Automotive

Requirements
Must have
• Tie in with business cards. So it needs grey tones with green and white logo. Name, address, phone and web address. Must have 8.5 x 11 paper and envelopes.
Nice to have
• Jot tab notes

```html
<!DOCTYPE html>
<html lang="en">
<head>
<meta charset="utf-8">
<title>Dentwise Auto Stationery</title>
<link rel="stylesheet" href="https://fonts.googleapis.com/css2?family=Arimo:wght@400;700&display=swap">
<style>
  :root {
    --lime: #80ff00;
    --lime-soft: #c9f7a0;
    --grey-top: #cfcfcf;
    --grey-mid: #e6e6e6;
    --paper: #ffffff;
    --ink: #111111;
    --edge: #555555;
    --body-font: "Arimo", Arial, sans-serif;
  }
  * { box-sizing: border-box; margin: 0; padding: 0; }
  html, body { width: 1200px; height: 720px; overflow: hidden; background: var(--paper); }
  body { position: relative; font-family: var(--body-font); color: var(--ink); }

  .brand { position: absolute; }
  .brand-name {
    font-family: var(--body-font);
    font-weight: 700;
    color: var(--lime);
    letter-spacing: -0.3px;
    line-height: 1;
    white-space: nowrap;
  }

  .swoosh-area {
    position: absolute;
    background: linear-gradient(to bottom, rgba(200,247,160,0) 0%, var(--lime-soft) 55%, var(--lime) 70%, rgba(255,255,255,0) 100%);
    border-radius: 60% 40% 10% 10% / 100% 100% 20% 20%;
    opacity: .85;
  }

  .contact { position: absolute; white-space: nowrap; }
  .contact.right { text-align: right; }

  /* Envelope front */
  .envelope-front {
    position: absolute; left: 0; top: 59px; width: 581px; height: 213px;
    background: linear-gradient(to bottom, var(--grey-top) 0%, var(--grey-mid) 45%, var(--paper) 85%);
  }
  .envelope-front .brand { left: 25px; top: 36px; }
  .envelope-front .brand-name { font-size: 15px; }
  .envelope-front .swoosh-area { left: 20px; top: 150px; width: 546px; height: 80px; }
  .envelope-front .contact { font-size: 8px; line-height: 14px; }
  .envelope-front .contact.left { left: 26px; top: 218px; }
  .envelope-front .contact.right { right: 28px; top: 216px; }

  /* Envelope back */
  .envelope-back {
    position: absolute; left: 9px; top: 370px; width: 581px; height: 255px;
    border: 1px solid var(--edge); background: var(--paper);
  }
  .envelope-back svg { position: absolute; left: -1px; top: -1px; }

  /* Letterhead */
  .letterhead {
    position: absolute; left: 644px; top: 0; width: 556px; height: 720px;
    border: 1px solid #9a9a9a;
    background: linear-gradient(to bottom, var(--grey-top) 0%, #e2e2e2 50%, var(--paper) 100%);
  }
  .letterhead .brand { left: 48px; top: 58px; }
  .letterhead .brand-name { font-size: 19px; }
  .letterhead .swoosh-area { left: 12px; top: 585px; width: 532px; height: 80px; }
  .letterhead .contact { font-size: 9px; line-height: 17px; }
  .letterhead .contact.left { left: 31px; top: 669px; }
  .letterhead .contact.right { right: 38px; top: 680px; }
</style>
</head>
<body>

<section class="envelope-front">
  <div class="brand">
    <div class="brand-name">Dentwise Auto</div>
  </div>
  <div class="swoosh-area" role="img" aria-label="Flowing green car silhouette swoosh"></div>
  <div class="contact left">Dentwise Auto<br>88 Panel Street Brookfield 3010</div>
  <div class="contact right">M: 0400 123 456 T: 03 5550 1234<br>E: mia@dentwiseauto.com W: www.dentwiseauto.com</div>
</section>

<section class="envelope-back">
  <svg width="583" height="105" viewBox="0 0 583 105" aria-hidden="true">
    <path d="M0 0 H583 V70 L576 85 Q570 102 555 102 H30 Q18 102 12 92 L4 72 V0 Z" fill="var(--lime)"/>
  </svg>
</section>

<section class="letterhead">
  <div class="brand">
    <div class="brand-name">Dentwise Auto</div>
  </div>
  <div class="swoosh-area" role="img" aria-label="Flowing green car silhouette swoosh"></div>
  <div class="contact left">M: 0400 123 456 T: 03 5550 1234<br>E: mia@dentwiseauto.com W: www.dentwiseauto.com</div>
  <div class="contact right">88 Panel Street Brookfield 3010</div>
</section>

</body>
</html>
```